Staffing/Recruitment company

We need to upgrade our website. At the moment we have a template that was built last year and looks not good at all.
We would like to update it with a new design based on what is popular this year. Including some visual effects etc.
This website is to give all information to our potential clients about what we do, clients with worked in the past, how to contact us and about us.
The website consists of 4 pages.
We would like to see a design that uses the color blue.
The current website is https://brightlanestaff.us/
Logo of the company is uploaded

Some designs were not complete...

```html
<!DOCTYPE html>
<html lang="en">
<head>
<meta charset="utf-8">
<title>Brightlane Staff – Staffing &amp; Recruitment</title>
<link href="https://fonts.googleapis.com/css2?family=Poppins:wght@400;500;600;700;800&display=swap" rel="stylesheet">
<style>
:root{
  --navy:#11124f;
  --navy-deep:#0b0c3d;
  --orange:#f05a28;
  --text:#2b2b33;
  --muted:#55566a;
  --line:#d9d9e0;
  --white:#ffffff;
  --contact-band:#1d2072;
}
*{box-sizing:border-box;margin:0;padding:0}
html,body{width:1200px;height:3454px;overflow:hidden;background:var(--white)}
body{font-family:"Poppins",sans-serif;color:var(--text);position:relative}
.page{position:relative;width:1200px;height:3454px;overflow:hidden}
.abs{position:absolute}
.center{left:0;width:1200px;text-align:center}

/* header */
.brand{display:flex;align-items:center;gap:8px;font-weight:700;color:var(--navy);font-size:18px;letter-spacing:.2px}
.brand-square{width:44px;height:44px;background:var(--navy);border-radius:4px}
.site-brand{left:98px;top:34px}
.main-nav{left:424px;top:46px;display:flex;gap:28px;font-size:17px;font-weight:500;color:var(--navy)}
.main-nav .active{position:relative}
.main-nav .active::after{content:"";position:absolute;left:0;top:30px;width:44px;height:4px;background:var(--orange);border-radius:2px}
.main-nav .active::before{content:"";position:absolute;left:42px;top:25px;width:10px;height:10px;border:3px solid var(--orange);border-radius:50%;background:#fff}
.btn{display:flex;align-items:center;justify-content:center;background:var(--orange);color:#fff;font-weight:600;border-radius:6px;box-shadow:0 4px 10px rgba(240,90,40,.35)}
.login{left:861px;top:36px;width:173px;height:43px;font-size:18px}

/* hero */
.hatch{left:-60px;top:122px;width:200px;height:230px;border-radius:0 115px 115px 0;background:#f1f1f3}
.hero-welcome{left:99px;top:226px;font-size:44px;font-weight:600;color:var(--orange);letter-spacing:1px}
.hero-title{left:97px;top:286px;font-size:66px;line-height:84px;font-weight:800;color:var(--navy);letter-spacing:1px}
.hero-tag{left:99px;top:466px;font-size:24px;color:var(--text)}
.get-started{left:100px;top:536px;width:171px;height:54px;font-size:18px}
.accent-band{height:30px;border-radius:3px;background:linear-gradient(180deg,rgba(17,18,79,.18) 0 45%,rgba(240,90,40,.25) 55% 100%)}
.hero-art{left:560px;top:0;width:640px;height:760px}

/* section headings */
.sec-title{font-size:39px;font-weight:800;color:var(--navy);letter-spacing:.5px}
.sec-sub{font-size:20px;font-weight:600;color:var(--orange);letter-spacing:.5px}

/* services */
.hex{width:327px;height:377px;clip-path:polygon(50% 0,100% 25%,100% 75%,50% 100%,0 75%,0 25%);color:#fff;text-align:center;display:flex;flex-direction:column;justify-content:center;align-items:center;padding:128px 16px 0}
.hex h3{font-size:19px;font-weight:700;line-height:31px;margin-bottom:10px}
.hex p{font-size:16px;line-height:24px}
.hex a{color:#fff;font-weight:600;text-decoration:underline}
.hex-a{left:99px;top:935px;background:linear-gradient(180deg,#7a4a5e 0%,#8e5148 55%,#e3602c 100%)}
.hex-b{left:436px;top:935px;background:linear-gradient(180deg,#9aa0a6 0%,#4b4e55 55%,#000 100%)}
.hex-b h3{line-height:24px}
.hex-c{left:774px;top:935px;background:linear-gradient(180deg,#6f4c6e 0%,#8a5560 55%,#e65e2a 100%)}

/* about band */
.about{left:0;top:1391px;width:1200px;height:430px;background:linear-gradient(180deg,#4b2468 0%,#6e3552 55%,#c85a30 100%)}
.about-title{top:1438px;color:#fff}
.about-sub{top:1497px;font-size:20px;font-weight:600;color:#fff}
.about-text{left:140px;top:1558px;width:920px;text-align:center;font-size:16px;line-height:26px;color:#fff}
.outline-btn{left:534px;top:1723px;width:132px;height:45px;border:2px solid #fff;border-radius:6px;color:#fff;font-size:15px;font-weight:600;display:flex;align-items:center;justify-content:center}

/* clients */
.client{width:234px;height:159px;border:2px solid var(--line);display:flex;align-items:center;justify-content:center;gap:8px;font-size:18px;font-weight:600;color:var(--navy);background:#fff}
.client.featured{border-color:#f2b8a6;box-shadow:0 3px 10px rgba(240,90,40,.2)}
.client .dot{width:14px;height:14px;border-radius:50%;background:var(--orange)}

/* contact band */
.touch{left:0;top:2266px;width:1200px;height:517px;background:linear-gradient(180deg,#23267a 0%,var(--contact-band) 60%,#181a62 100%)}
.touch-title{top:2300px;color:#fff;font-weight:600;font-size:36px}
.touch-rule{left:566px;top:2352px;width:68px;height:4px;background:#fff}
.field{background:#fff;border-radius:12px;font-size:13px;color:#8a8a96;padding:16px 12px}
.submit{left:527px;top:2690px;width:146px;height:47px;font-size:20px;border-radius:6px}

/* join */
.join-title{top:2822px;font-size:36px;font-weight:500;color:var(--navy)}
.join-text{left:180px;top:2893px;width:840px;text-align:center;font-size:15px;line-height:26px;color:var(--muted)}
.join-btn{left:544px;top:2962px;width:129px;height:49px;font-size:20px}
.divider{left:0;top:3073px;width:1200px;height:1px;background:#e6e6ea}

/* footer */
.foot-brand{left:0;width:1200px;top:3128px;justify-content:center}
.info{display:flex;align-items:center;gap:12px}
.info .ico{width:38px;height:38px;border-radius:50%;background:var(--navy);display:flex;align-items:center;justify-content:center}
.info b{display:block;font-size:12px;font-weight:600;color:var(--navy)}
.info span{font-size:15px;color:var(--text)}
.foot-bar{left:0;top:3307px;width:1200px;height:68px;background:var(--orange);display:flex;justify-content:center;align-items:center;gap:28px;color:#fff;font-size:18px;font-weight:500}
.copyright{top:3398px;font-size:15px;font-weight:500;color:var(--navy-deep)}
</style>
</head>
<body>
<div class="page">

  <!-- header -->
  <div class="abs brand site-brand"><span class="brand-square"></span>BRIGHTLANE STAFF</div>
  <nav class="abs main-nav">
    <span class="active">HOME</span><span>CLIENTS</span><span>ABOUT US</span><span style="margin-left:4px">CONTACT US</span>
  </nav>
  <div class="abs btn login">LOGIN</div>

  <!-- hero -->
  <div class="abs hatch" role="img" aria-label="Faint diagonal hatch ornament"></div>
  <div class="abs hero-welcome">WELCOME TO</div>
  <div class="abs hero-title">BRIGHTLANE<br>STAFF</div>
  <div class="abs hero-tag">Staffing &amp; Recruitment Company.</div>
  <div class="abs btn get-started">GET STARTED</div>
  <div class="abs accent-band" style="left:98px;top:676px;width:222px" role="img" aria-label="Navy and orange zigzag ornament"></div>

  <svg class="abs hero-art" viewBox="560 0 640 760">
    <defs>
      <linearGradient id="heroPhoto" x1="0" y1="0" x2="1" y2="1">
        <stop offset="0" stop-color="#8d9aa8"/>
        <stop offset=".5" stop-color="#5e6e80"/>
        <stop offset="1" stop-color="#262a33"/>
      </linearGradient>
    </defs>
    <circle cx="1020" cy="-10" r="40" fill="none" stroke="var(--navy)" stroke-width="16"/>
    <polygon points="1040,20 1200,110 1200,480 1170,480 1170,130 1020,40" fill="var(--navy)"/>
    <polygon points="886,96 1176,260 1176,580 886,744" fill="none" stroke="var(--navy)" stroke-width="14"/>
    <polygon points="598,194 650,215 650,600 800,690 770,710 598,600" fill="var(--orange)"/>
    <circle cx="800" cy="712" r="34" fill="none" stroke="var(--orange)" stroke-width="14"/>
    <polygon role="img" aria-label="Photo of a smiling recruiter with glasses holding a pen at an interview table" points="886,100 1177,262 1177,582 886,744 617,582 617,262" fill="url(#heroPhoto)"/>
  </svg>

  <!-- services -->
  <div class="abs center sec-title" style="top:832px">WHAT WE DO</div>
  <div class="abs center sec-sub" style="top:892px">OUR SERVICES</div>

  <div class="abs hex hex-a" role="img" aria-label="Team of colleagues shaking hands in an office">
    <h3>Hire Top Professional<br>SDETS</h3>
    <p>We work with elite test-automation<br>engineers. <a>LEARN MORE</a></p>
  </div>
  <div class="abs hex hex-b" role="img" aria-label="Colleagues working together at a laptop in an open office">
    <h3>Let Us Build End To End<br>Automated QA Infrastructure</h3>
    <p>We can safe your time and budget.<br><a>LEARN MORE</a></p>
  </div>
  <div class="abs hex hex-c" role="img" aria-label="Group of professionals seated in a meeting">
    <h3>Request Instructor For<br>Your Team</h3>
    <p>We are committed to helping<br>companies. <a>LEARN MORE</a></p>
  </div>

  <!-- about -->
  <div class="abs about" role="img" aria-label="Background photo of people in a business meeting under a purple to orange tint"></div>
  <div class="abs center sec-title about-title">WHO WE ARE</div>
  <div class="abs center about-sub">ABOUT US</div>
  <p class="abs about-text">Day in and day out for the last years we've been more than just a staffing company. Throughout this time we've built relationships, we've grown together internally and externally, and have created a system that allows us to personally cater to the needs of our clients and candidates. We've been a mentor for some, a team builder for others, but most importantly we've been there. We know there is no substitute for experience, so let us help you navigate through the ever changing web of talent.</p>
  <div class="abs outline-btn">LEARN MORE</div>

  <!-- clients -->
  <div class="abs center sec-title" style="top:1900px">OUR CLIENTS</div>
  <div class="abs center sec-sub" style="top:1962px">OUR POTENTIAL CLIENTS</div>
  <div class="abs accent-band" style="left:1030px;top:1906px;width:170px" role="img" aria-label="Navy and orange zigzag ornament"></div>
  <div class="abs client" style="left:113px;top:2020px"><span class="dot"></span>Kestrelwise</div>
  <div class="abs client featured" style="left:361px;top:2020px"><span class="dot"></span>Tradevane</div>
  <div class="abs client" style="left:607px;top:2020px"><span class="dot"></span>Orbitalia</div>
  <div class="abs client" style="left:854px;top:2020px"><span class="dot"></span>Halcyra</div>

  <!-- contact -->
  <div class="abs touch" role="img" aria-label="Background photo of a handshake under a deep blue tint"></div>
  <div class="abs center touch-title">GET IN TOUCH</div>
  <div class="abs touch-rule"></div>
  <div class="abs field" style="left:98px;top:2390px;width:488px;height:51px">First Name*</div>
  <div class="abs field" style="left:603px;top:2390px;width:497px;height:51px">Last Name*</div>
  <div class="abs field" style="left:98px;top:2454px;width:488px;height:50px">Email*</div>
  <div class="abs field" style="left:603px;top:2454px;width:497px;height:50px">Your Company*</div>
  <div class="abs field" style="left:98px;top:2520px;width:999px;height:118px;padding-top:12px">Comments</div>
  <div class="abs btn submit">SUBMIT</div>

  <!-- join -->
  <div class="abs center join-title">JOIN OUR CAREER NETWORK</div>
  <p class="abs join-text">Our Career Network will enhance your job search and application process. Whether you choose to apply or just leave your information, we look forward to staying connected with you.</p>
  <div class="abs btn join-btn">JOIN</div>
  <div class="abs accent-band" style="left:0;top:3038px;width:158px" role="img" aria-label="Navy and orange zigzag ornament"></div>
  <div class="abs divider"></div>

  <!-- footer -->
  <div class="abs brand foot-brand"><span class="brand-square"></span>BRIGHTLANE STAFF</div>
  <div class="abs info" style="left:334px;top:3232px">
    <span class="ico"><svg width="16" height="12" viewBox="0 0 16 12"><rect x="1" y="1" width="14" height="10" rx="1" fill="none" stroke="#fff" stroke-width="1.6"/><polyline points="1,1 8,7 15,1" fill="none" stroke="#fff" stroke-width="1.6"/></svg></span>
    <div><b>CONTACT MAIL</b><span>info@brightlanestaff.us</span></div>
  </div>
  <div class="abs info" style="left:615px;top:3232px">
    <span class="ico"><svg width="12" height="16" viewBox="0 0 12 16"><path d="M6 1a5 5 0 0 1 5 5c0 4-5 9-5 9S1 10 1 6a5 5 0 0 1 5-5z" fill="#fff"/><circle cx="6" cy="6" r="2" fill="var(--navy)"/></svg></span>
    <div><b>OUR LOCATION</b><span>2140 Cedar Ave, Fairview, VA</span></div>
  </div>
  <nav class="abs foot-bar"><span>HOME</span><span>CLIENTS</span><span>ABOUT US</span><span style="margin-left:4px">CONTACT US</span></nav>
  <div class="abs center copyright">Copyright © 2022 &nbsp;Brightlane Staff, LLC - All Rights Reserved.</div>

</div>
</body>
</html>
```